Commercial Janitorial Company needs a Postcard Design

We need a postcard design-i attached a sample-of one-not our industry-but same size and similar to content and what i am looking for-We are a commercial janitorial service-(not residential) we service High Tech-Bio Tech-Manufacturing-Office-Property Management Company'sThe design should incorporate Industry Services-Industries served website-company information-Two sided-color-our website: www.marlowcrestfacilitysvc.com will have information to use-bullet point type-should include Nice artwork-Attention grabbing headline then of course all our contact information found on website

The postcard is NOT a mailer but a hand-out (2 sides)-about 9" Long by 7" wide-

Target Market(s)

Commercial office Building's

Colors

Designer to choose colors to be used in the design.

Requirements
Must have
• All company information-website
• Services offered-Industries served
• Something mentioned about "Green Cleaning"
• Images of cleaning are good-in a commercial setting--Hi Tech-Bio Tech-Cleanroom Cleaning
• 24/7 access
• Locally owned and operated
• 25 Years in business
• Service Excellence
• With our highly-trained, in-house workforce, you can trust that we’ll provide you with services that increase efficiencies and lower your operating expenses—all while maintaining a uniform standard of service excellence.
• Breadth of Services
• We’ll provide you with an unrivaled range of facilities solutions that will keep your properties safe, clean, comfortable and energy efficient.
• Technology-Enabled Workforce
• Your facilities will be serviced with the support of innovative technology solutions that will simplify service delivery and allow for greater transparency.
• Guaranteed Sustainability Solutions
• We’ve got expertise to support all of your sustainability goals, including green cleaning, VORQ support, bundled energy solutions, and more.
• Size of Postcard is 9.5" length x 7" width
Should not have
• No Residential
• No Maid service
• No Cartoon type images
• Strickly commercial cleaning

```html
<!DOCTYPE html>
<html lang="en">
<head>
<meta charset="utf-8">
<title>Marlowcrest Facility Services – Commercial Cleaning Postcard</title>
<link rel="stylesheet" href="https://fonts.googleapis.com/css2?family=Oswald:wght@500;700&family=Barlow+Semi+Condensed:wght@700&family=Lato:wght@400;700;900&display=swap">
<style>
  :root {
    --brand-blue: #1b7dc6;
    --ink: #1c1c1c;
    --paper: #ffffff;
    --paper-shade: #e6e8eb;
    --backdrop: #e4e5e7;
    --alert-red: #d9232e;
    --photo-warm: #cfc8b8;
    --eco-green: #3aa53a;
  }
  * { box-sizing: border-box; margin: 0; padding: 0; }
  html, body { width: 1200px; height: 506px; overflow: hidden; }
  body { background: var(--backdrop); position: relative; font-family: "Lato", sans-serif; }

  .card { position: absolute; top: 56px; width: 536px; height: 394px; overflow: hidden; background: var(--paper); }
  .card--front { left: 56px; background: linear-gradient(90deg, var(--paper) 0%, var(--paper-shade) 100%); }
  .card--back { left: 610px; }

  /* Front */
  .scene-art { position: absolute; left: 0; top: 0; width: 536px; height: 394px; }

  .headline-top { position: absolute; left: 20px; top: 16px; font: 500 33px/1 "Oswald", sans-serif; color: var(--brand-blue); white-space: nowrap; }
  .headline-main { position: absolute; left: 18px; top: 52px; font: 700 72px/1 "Oswald", sans-serif; color: var(--ink); letter-spacing: 0.5px; white-space: nowrap; }
  .years-band { position: absolute; left: 0; top: 137px; width: 276px; height: 17px; background: var(--brand-blue); color: var(--paper); font: 500 9.6px/17px "Oswald", sans-serif; padding-left: 20px; letter-spacing: 0.2px; white-space: nowrap; }

  .feature-list { position: absolute; left: 0; top: 164px; width: 186px; list-style: none; }
  .feature { display: flex; align-items: center; height: 52px; padding-left: 24px; border-bottom: 2px solid var(--brand-blue); }
  .feature:last-child { border-bottom: 0; }
  .feature-icon { width: 36px; height: 36px; margin-right: 12px; flex: none; }
  .feature-label { font: 700 17px/18px "Barlow Semi Condensed", sans-serif; color: var(--ink); letter-spacing: 0.3px; white-space: nowrap; }

  .green-band { position: absolute; left: 0; bottom: 0; width: 300px; height: 62px; background: var(--brand-blue); color: var(--paper); font: 700 11.2px/14.5px "Lato", sans-serif; padding: 9px 0 0 20px; white-space: nowrap; }

  .photo-circle { position: absolute; border-radius: 50%; border: 4px solid var(--paper); box-shadow: 0 0 0 2px #c9cdd2; }
  .photo-circle--wall { left: 188px; top: 160px; width: 104px; height: 104px; background: linear-gradient(160deg, #d7dbd5, #8aa69a); }
  .photo-circle--floor { left: 240px; top: 228px; width: 136px; height: 136px; background: linear-gradient(160deg, #eeeeee, #b7c2c9); }

  .sustain-seal { position: absolute; left: 272px; top: 140px; width: 72px; height: 72px; border-radius: 50%; background: var(--paper); border: 2px solid #2c5f8f; display: flex; align-items: center; justify-content: center; text-align: center; font: 700 11px/11.5px "Barlow Semi Condensed", sans-serif; color: var(--alert-red); }

  /* Back */
  .company-name { position: absolute; left: 28px; top: 26px; width: 176px; font: 900 22px/1.1 "Lato", sans-serif; color: var(--brand-blue); }
  .eco-seal { position: absolute; left: 212px; top: 34px; width: 84px; height: 84px; border-radius: 50%; background: radial-gradient(circle at 40% 35%, #8fd36b, var(--eco-green) 60%, #1f7a2a); }
  .stamp-box { position: absolute; left: 464px; top: 22px; width: 56px; height: 56px; background: var(--ink); }

  .services-panel { position: absolute; left: 0; top: 138px; width: 308px; height: 174px; background: var(--ink); border-radius: 0 87px 87px 0; }
  .service { position: absolute; left: 0; display: flex; }
  .service--excellence { top: 16px; }
  .service--breadth { top: 74px; }
  .service--tech { top: 122px; }
  .service-icon { width: 28px; height: 28px; margin: 4px 14px 0 26px; flex: none; }
  .service-copy { width: 218px; }
  .service-title { font: 900 10px/1.15 "Lato", sans-serif; color: var(--paper); letter-spacing: 0.2px; white-space: nowrap; }
  .service-text { font: 400 6.6px/1.32 "Lato", sans-serif; color: var(--paper); margin-top: 1px; }

  .contact { position: absolute; left: 25px; top: 332px; color: var(--brand-blue); font-style: normal; }
  .contact-address { font: 700 11.5px/1.2 "Lato", sans-serif; }
  .contact-phone { font: 700 20px/1.2 "Lato", sans-serif; }
  .contact-web { font: 700 10.5px/1.2 "Lato", sans-serif; }
</style>
</head>
<body>

<section class="card card--front" aria-label="Postcard front">
  <svg class="scene-art" viewBox="0 0 536 394">
    <path d="M446 0 C330 70 290 250 300 394 L536 394 L536 0 Z" fill="var(--photo-warm)" role="img" aria-label="Photo of a janitorial cart with yellow mop bucket, mops and wet floor sign in a commercial corridor"/>
    <path d="M432 0 C316 70 276 250 286 394" fill="none" stroke="var(--brand-blue)" stroke-width="14"/>
  </svg>

  <h1 class="headline-top">EFFECTIVE COMMERCIAL</h1>
  <p class="headline-main">CLEANING</p>
  <p class="years-band">25 YEARS SERVING SAN JOSE AND THE SURROUNDING AREAS</p>

  <ul class="feature-list">
    <li class="feature">
      <svg class="feature-icon" viewBox="0 0 36 36" fill="none" stroke="var(--brand-blue)" stroke-width="2">
        <rect x="4" y="12" width="12" height="20"/><rect x="16" y="4" width="14" height="28"/>
        <path d="M20 9h2M25 9h2M20 15h2M25 15h2M20 21h2M25 21h2M7 17h2M11 17h2M7 23h2M11 23h2M2 33h32"/>
      </svg>
      <span class="feature-label">INDUSTRIES<br>SERVED</span>
    </li>
    <li class="feature">
      <svg class="feature-icon" viewBox="0 0 36 36" fill="none" stroke="var(--brand-blue)" stroke-width="2">
        <path d="M31 18a13 13 0 1 1-4-9.5"/><path d="M28 3v6h-6"/>
        <text x="11" y="22" font-size="10" font-family="Lato, sans-serif" font-weight="900" fill="var(--brand-blue)" stroke="none">24</text>
      </svg>
      <span class="feature-label">24/7<br>ACCESS</span>
    </li>
    <li class="feature">
      <svg class="feature-icon" viewBox="0 0 36 36" fill="none" stroke="var(--brand-blue)" stroke-width="2">
        <path d="M4 30l8-4 12 4 8-4V10l-8 4-12-4-8 4z"/>
        <path d="M22 4a5 5 0 0 1 5 5c0 4-5 9-5 9s-5-5-5-9a5 5 0 0 1 5-5z" fill="var(--paper)"/>
        <circle cx="22" cy="9" r="1.6"/>
      </svg>
      <span class="feature-label">LOCALLY OWNED<br>&amp; OPERATED</span>
    </li>
  </ul>

  <p class="green-band">We’ve got expertise to support all of your<br>sustainability goals, including green cleaning,<br>VORQ support, bundled energy solutions, and more.</p>

  <div class="photo-circle photo-circle--wall" role="img" aria-label="Photo of a cleaner wiping a wall beside a service cart"></div>
  <div class="photo-circle photo-circle--floor" role="img" aria-label="Photo of a cleaner mopping an office floor"></div>
  <p class="sustain-seal">Guaranteed<br>Sustainability<br>Solutions</p>
</section>

<section class="card card--back" aria-label="Postcard back">
  <p class="company-name">Marlowcrest Facility Services Inc.</p>
  <div class="eco-seal" role="img" aria-label="Eco-friendly seal"></div>
  <div class="stamp-box" aria-hidden="true"></div>

  <div class="services-panel">
    <div class="service service--excellence">
      <svg class="service-icon" viewBox="0 0 30 30" fill="none" stroke="var(--paper)" stroke-width="1.8">
        <path d="M3 14h12l-2 13H5z"/><path d="M22 2v18M18 20h8l1 8h-10z"/>
      </svg>
      <div class="service-copy">
        <h2 class="service-title">SERVICE EXCELLENCE</h2>
        <p class="service-text">With our highly-trained, in-house workforce, you can trust that we’ll provide you with services that increase efficiencies and lower your operating expenses—all while maintaining a uniform standard of service excellence.</p>
      </div>
    </div>
    <div class="service service--breadth">
      <svg class="service-icon" viewBox="0 0 30 30" fill="none" stroke="var(--paper)" stroke-width="1.8">
        <path d="M4 9c4-4 9-5 13-2l-3 3"/><path d="M26 21c-4 4-9 5-13 2l3-3"/><path d="M18 11v8M18 11l-2 2M18 19l2-2"/>
      </svg>
      <div class="service-copy">
        <h2 class="service-title">BREADTH OF SERVICES</h2>
        <p class="service-text">We’ll provide you with an unrivaled range of facilities solutions that will keep your properties safe, clean, comfortable and energy efficient.</p>
      </div>
    </div>
    <div class="service service--tech">
      <svg class="service-icon" viewBox="0 0 30 30" fill="none" stroke="var(--paper)" stroke-width="1.8">
        <path d="M14 3h4v12h-4z"/><path d="M10 15h12v6H10z"/><circle cx="8" cy="24" r="4"/><path d="M12 24h12"/>
      </svg>
      <div class="service-copy">
        <h2 class="service-title">TECHNOLOGY-ENABLED WORKFORCE</h2>
        <p class="service-text">Your facilities will be serviced with the support of innovative technology solutions that will simplify service delivery and allow for greater transparency.</p>
      </div>
    </div>
  </div>

  <address class="contact">
    <p class="contact-address">2740 Alder Ridge Way #C, San Jose, CA 95112</p>
    <p class="contact-phone">Phone: 408-555-0172</p>
    <p class="contact-web">www.marlowcrestfacilitysvc.com</p>
  </address>
</section>

</body>
</html>
```